Ad Banner for Expert Web Board

This banner is used in "Lantern Quay" web site. This web site provides a single place for all employees to ask questions related to work. There will be dedicated subject matter experts to respond to all questions. The web site also provides "Maple Ledger" where employee can see the list of all experts in the company.
1. Banner size: 940x380
2. Business background: Provides maintenance, design and engineering, construction, machinery operation, material procurement and production management services for petrochemical and refinery business
3. We would like to see designs that
- Promote the ask questions in "Lantern Quay" system
- Promote that company has experts in the areas of "Maintenance and Engineering" and can be found in "Maple Ledger"
- Encourage employees to advocate himself to be an expert by sending an email to a specific email address.
- Do not include picture of real people in the banner

```html
<!DOCTYPE html>
<html lang="en">
<head>
<meta charset="utf-8">
<title>Lantern Quay – Banner</title>
<link rel="stylesheet" href="https://fonts.googleapis.com/css2?family=Roboto+Condensed:wght@400;700&family=Roboto:wght@300&display=swap">
<style>
  :root {
    --banner-blue: #2d6899;
    --accent-blue: #6a94b9;
    --text-white: #ffffff;
  }
  html, body {
    margin: 0;
    padding: 0;
    width: 1200px;
    height: 485px;
    overflow: hidden;
    background: var(--banner-blue);
  }
  .banner {
    position: relative;
    width: 1200px;
    height: 485px;
    background: var(--banner-blue);
    overflow: hidden;
    font-family: "Roboto", Arial, sans-serif;
    color: var(--text-white);
  }
  .banner__art {
    position: absolute;
    inset: 0;
    width: 1200px;
    height: 485px;
  }
  .banner__accent {
    fill: var(--accent-blue);
  }
  .banner__title {
    font-family: "Roboto Condensed", "Arial Narrow", sans-serif;
    font-weight: 700;
    fill: var(--text-white);
  }
  .banner__tagline {
    position: absolute;
    left: 51px;
    top: 280px;
    margin: 0;
    font-family: "Roboto Condensed", "Arial Narrow", sans-serif;
    font-weight: 400;
    font-size: 18.6px;
    line-height: 1;
    white-space: nowrap;
    letter-spacing: -0.1px;
  }
  .contact {
    position: absolute;
    top: 380px;
    left: 56px;
    display: flex;
    align-items: center;
  }
  .contact__item {
    display: flex;
    align-items: center;
    font-weight: 300;
    font-size: 34px;
    line-height: 1;
    white-space: nowrap;
  }
  .contact__item--phone { width: 406px; }
  .contact__item--phone .contact__icon { margin-right: 17px; }
  .contact__item--email .contact__icon { margin-right: 22px; }
  .phone-digits { word-spacing: 10px; }
</style>
</head>
<body>
  <div class="banner">
    <svg class="banner__art" viewBox="0 0 1200 485">
      <circle class="banner__accent" cx="1085" cy="200" r="72"/>
      <text class="banner__title" x="51" y="246" font-size="152">Lantern Quay</text>
    </svg>

    <p class="banner__tagline">Company has experts in the areas of "Maintenance and Engineering" and can be found in "Maple Ledger"</p>

    <div class="contact">
      <div class="contact__item contact__item--phone">
        <svg class="contact__icon" width="56" height="54" viewBox="0 0 56 54" aria-hidden="true">
          <rect x="0" y="0" width="56" height="54" rx="9" fill="#ffffff"/>
          <path d="M19 10c2-1 4-1 5 1l3 7c1 2 0 3-1 4l-2 2c1 4 5 9 9 11l2-2c1-1 3-2 4-1l6 4c2 1 2 3 1 5l-2 3c-2 2-5 3-8 2-10-4-18-13-21-24-1-3 0-6 2-8z" fill="var(--banner-blue)"/>
          <path d="M33 12c5 1 9 5 10 10M33 18c2 0 4 2 4 4" stroke="var(--banner-blue)" stroke-width="2.4" fill="none" stroke-linecap="round"/>
        </svg>
        <span class="phone-digits">0000 0000 0000</span>
      </div>
      <div class="contact__item contact__item--email">
        <svg class="contact__icon" width="59" height="46" viewBox="0 0 59 46" aria-hidden="true">
          <rect x="1.5" y="1.5" width="56" height="43" fill="none" stroke="#ffffff" stroke-width="3"/>
          <path d="M2 3l27.5 24L57 3" fill="none" stroke="#ffffff" stroke-width="3"/>
          <path d="M2 44l21-20M57 44L36 24" fill="none" stroke="#ffffff" stroke-width="3"/>
        </svg>
        <span>lanternquay@info.com</span>
      </div>
    </div>
  </div>
</body>
</html>
```